Exciting, Bold and Modern Landscaping & Turf care company business card

Hello, I own a lawn and landscaping company in Virginia, USA. We would like to design a bold, dynamic, modern business card that really makes us stand out. I tire of all green business cards with crappy, cartoonish clipart grass on them. It needs to be two sided, on one side i need to highlight our turf care division called "Promised Brighter Meadow" We maintain grass, fertilize it, weed control, etc.. We have a green thumbed gopher as our logo that i will attach. I am looking for something, clean and neat but out of the box in style. Im open to all ideas, and would like different options for them. On the other side, i want to highlight our landscaping division "Quiet Harbor Landscaping" In this division we design and install landscapes. Feel free to visit our website for more info or email me with ANY questions. Our busines cards in the past have highlighted our different services, but i don't want to this time. By the time I hand out a business card we are usually already estimating a project and they know what services we offer. I do want them to look at my card and say "wow thats pretty cool" and for them to think "These guys are something different, not just your standard dirt diggers" The logo doesnt have to be on both sides, but it needs to be on the turf care side. Our phone number and website should also be on at least on side, but need not be on both. The phone number is (555)618-4072 as well as the web address as www.MossbrookYardWorks.example. I like for the web address to have caps like that becasue it makes the long address much easier to read. I would like it in full color, printing costs are not my major concern. I also love rounded corners or interesting die cut designs as well, so feel free to wow me. Whether it be a clean white background with a bold photo to an all black card with a gray logo except for his green thumb with silver foil lettering to anything in between, lets go for it. That bieng said i dont want anything cartoonish, we are still a professional service and i want that to come through. THANKS!
Updates
Project Deadline Extended
Reason: changed project to a committed payment. I would like designers to re-evaluate their interest now and give them extra time to submit designs. Thank you.
we have changed our status to a commited payment to entice more submissions. thank you all for your hard work!
Industry/Entity Type
Professional Service
Look and feel
Each slider illustrates characteristics of the customer's brand and the style your logo design should communicate.

```html
<!DOCTYPE html>
<html lang="en">
<head>
<meta charset="utf-8">
<title>Quiet Harbor Landscaping – Business Card</title>
<link href="https://fonts.googleapis.com/css2?family=Open+Sans:wght@400;600;700&display=swap" rel="stylesheet">
<style>
  :root {
    --page: #e9e7e2;
    --green-dark: #1f7a2a;
    --green: #2f9a38;
    --green-light: #4db346;
    --orange: #e8901c;
    --orange-light: #f4ae3c;
    --white: #ffffff;
    --paper: #f3f3f1;
    --mascot-fur: #e0a04a;
    --mascot-belly: #f6efe2;
  }
  * { box-sizing: border-box; margin: 0; padding: 0; }
  html, body { width: 1200px; height: 902px; overflow: hidden; }
  body {
    background: var(--page);
    font-family: "Open Sans", sans-serif;
    display: flex;
    align-items: center;
    justify-content: center;
    gap: 40px;
  }
  .card {
    position: relative;
    width: 560px;
    height: 320px;
    border-radius: 22px;
    overflow: hidden;
    box-shadow: 0 6px 18px rgba(0,0,0,.18);
  }

  /* Front: turf care side */
  .card-front {
    background: radial-gradient(ellipse at 60% 40%, var(--green-light), var(--green) 45%, var(--green-dark));
  }
  .front-title {
    position: absolute;
    top: 34px;
    right: 34px;
    text-align: right;
    color: var(--white);
    font-weight: 700;
    font-size: 21px;
    line-height: 1.3;
  }
  .front-mascot {
    position: absolute;
    left: 30px;
    bottom: 0;
    width: 250px;
    height: 170px;
    border-radius: 80px 80px 0 0;
    background: linear-gradient(180deg, var(--mascot-fur) 0%, var(--mascot-fur) 55%, var(--mascot-belly) 75%, var(--green-light) 100%);
  }

  /* Back: contact side */
  .card-back { background: var(--paper); }
  .card-back svg.bands { position: absolute; inset: 0; }
  .back-title {
    position: absolute;
    left: 150px;
    top: 34px;
    color: var(--green);
    font-weight: 600;
    font-size: 16px;
    line-height: 1.35;
  }
  .back-mascot {
    position: absolute;
    left: 24px;
    top: 110px;
    width: 118px;
    height: 92px;
    border-radius: 50px 50px 10px 10px;
    background: linear-gradient(180deg, var(--mascot-fur) 0%, var(--mascot-fur) 60%, var(--mascot-belly) 85%, var(--green-light) 100%);
  }
  .person {
    position: absolute;
    left: 40px;
    top: 214px;
    color: var(--white);
  }
  .person-name { font-weight: 700; font-size: 18px; line-height: 1.2; }
  .person-role { font-size: 12px; }
  .phone {
    position: absolute;
    left: 40px;
    bottom: 14px;
    color: var(--green);
    font-weight: 600;
    font-size: 15px;
  }
  .contact {
    position: absolute;
    right: 22px;
    top: 130px;
    list-style: none;
    color: var(--white);
    font-size: 12px;
    text-align: right;
    line-height: 1.55;
  }
  .contact li { display: flex; justify-content: flex-end; align-items: center; gap: 8px; }
  .contact li.gap { margin-top: 12px; }
  .contact svg { width: 12px; height: 12px; flex: none; }
  .contact .spacer { width: 12px; flex: none; }
</style>
</head>
<body>

  <section class="card card-front">
    <h1 class="front-title">Quiet Harbor Landscaping and<br>Promised Brighter Meadow</h1>
    <div class="front-mascot" role="img" aria-label="Gopher mascot giving a green thumbs-up in grass"></div>
  </section>

  <section class="card card-back">
    <svg class="bands" viewBox="0 0 560 320" aria-hidden="true">
      <path d="M0,205 C220,200 380,150 470,0 L560,0 L560,262 L0,262 Z" fill="var(--orange)"/>
      <path d="M-5,205 C220,200 380,150 470,-5" fill="none" stroke="var(--green)" stroke-width="14"/>
      <rect x="0" y="262" width="560" height="9" fill="var(--green)"/>
    </svg>

    <div class="back-mascot" role="img" aria-label="Gopher mascot giving a green thumbs-up"></div>
    <h2 class="back-title">Quiet Harbor Landscaping<br>and Promised Brighter Meadow</h2>

    <ul class="contact">
      <li>4870-12 Linden Rd, Suite 118,
        <svg viewBox="0 0 12 12"><rect x="1" y="4" width="10" height="7" fill="none" stroke="#fff" stroke-width="1.4"/><path d="M1,4 L6,1 L11,4" fill="none" stroke="#fff" stroke-width="1.4"/></svg></li>
      <li>Harborview, VA 23999<span class="spacer"></span></li>
      <li>555.204.3391
        <svg viewBox="0 0 12 12"><path d="M3,1 L5,3.5 L4,5 C5,7 6,8 7,8.5 L8.5,7.5 L11,9.5 L9.5,11 C5,10.5 1.5,7 1,2.5 Z" fill="#fff"/></svg></li>
      <li class="gap">info@MossbrookYardWorks.example
        <svg viewBox="0 0 12 12"><rect x="1" y="3" width="10" height="7" fill="#fff"/><path d="M1,3 L6,7 L11,3" fill="none" stroke="var(--orange)" stroke-width="1"/></svg></li>
      <li>www.MossbrookYardWorks.example
        <svg viewBox="0 0 12 12"><circle cx="6" cy="6" r="5" fill="#fff"/><path d="M1,6 H11 M6,1 C3,4 3,8 6,11 M6,1 C9,4 9,8 6,11" fill="none" stroke="var(--orange)" stroke-width=".8"/></svg></li>
    </ul>

    <div class="person">
      <p class="person-name">Marco Ellison</p>
      <p class="person-role">General Manager</p>
    </div>

    <p class="phone">Phone : (555)618-4072</p>
  </section>

</body>
</html>
```